50% off blue price stickers - poster

I am looking for a poster to hang in our retail discount store that let's people know they take 50% off the marked price on anything with a blue price sticker. We try and tell them as they walk in but can't catch everyone. If they don't know, they don't see the value in the pricing. We mark the retail price with a blue price tag and they get 50% off that price. We sell items from wholesale clubs (Brindle, JETs Depot) and offer 50% off what they sell the items for. Clothes, Housewares, Kitchenware, Furniture, Bath and Body, Electronics, Jewelry - you name it.
Updates

Check out our Chirpbook page - Marla's Found Again, in Brentwood, California to learn more about us and our merchandise.

For poster size - we are looking at 20" wide by 30" long. Thank you.

Target Market(s)

Ages 35-50

Industry/Entity Type

Retail

Font styles to use
Serif

Requirements
Must have
• Store name - Marla's Found Again
Nice to have
• Not too cluttered - easy to read to get the point across quickly. Something that incorporates our logo - but doesn't have to stick with the red/black theme, especially if you are using blue themes in the poster. Maybe just use the theme of the logo so the fonts are similar....

```html
<!DOCTYPE html>
<html lang="en">
<head>
<meta charset="utf-8">
<title>Marla's Found Again – 50% Off Blue Price Tags</title>
<link rel="stylesheet" href="https://fonts.googleapis.com/css2?family=Anton&family=Barlow:wght@500;600&display=swap">
<style>
  :root {
    --night: #1b1a1b;
    --ember: #c0141b;
    --ember-deep: #6e0d10;
    --rust-top: #4a1a12;
    --rust-low: #7a2c1a;
    --paper: #ffffff;
    --ink: #ffffff;
    --tag-blue: #1f5fe0;
    --brand-red: #c8102e;
    --base-strip: #141414;
  }
  * { margin: 0; padding: 0; box-sizing: border-box; }
  html, body { width: 912px; height: 1200px; overflow: hidden; background: var(--night); }
  .poster {
    position: relative;
    width: 912px;
    height: 1200px;
    overflow: hidden;
    background:
      linear-gradient(to bottom, var(--night) 0%, var(--night) 52%, var(--rust-top) 62%, var(--rust-low) 78%, #8a3a26 90%);
  }
  .offer-disc {
    position: absolute;
    left: 156px; top: 100px;
    width: 560px; height: 540px;
    border-radius: 50%;
    border: 2px solid var(--ember);
    background:
      radial-gradient(ellipse at 62% 38%, #e0141c 0%, var(--ember) 28%, var(--ember-deep) 58%, rgba(40,20,22,0.9) 80%, rgba(27,26,27,0) 100%);
  }
  .headline { position: absolute; inset: 0; }
  .headline-figure, .headline-percent, .headline-off {
    position: absolute;
    font-family: "Anton", "Oswald", sans-serif;
    color: var(--ink);
    line-height: 1;
    text-shadow: 3px 3px 0 rgba(0,0,0,0.35);
  }
  .headline-figure { left: 184px; top: 196px; font-size: 272px; letter-spacing: -4px; }
  .headline-percent { left: 572px; top: 214px; font-size: 150px; }
  .headline-off { left: 532px; top: 420px; font-size: 94px; }
  .headline-slash { position: absolute; left: 0; top: 0; }
  .offer-terms {
    position: absolute;
    left: 0; right: 0; top: 672px;
    text-align: center;
    font-family: "Barlow", sans-serif;
    font-weight: 500;
    font-size: 54px;
    line-height: 74px;
    color: var(--ink);
  }
  .offer-terms .tag-colour { color: var(--tag-blue); }
  .brand-panel {
    position: absolute;
    left: 0; right: 0; top: 860px; height: 321px;
    background: linear-gradient(to bottom, rgba(255,255,255,0) 0%, var(--paper) 14%, var(--paper) 100%);
    display: flex;
    align-items: center;
    justify-content: center;
    gap: 26px;
    padding-top: 40px;
  }
  .brand-dot {
    width: 110px; height: 110px;
    border-radius: 50%;
    background: var(--brand-red);
  }
  .brand-name {
    font-family: "Barlow", sans-serif;
    font-weight: 600;
    font-size: 64px;
    color: var(--brand-red);
  }
  .base-strip {
    position: absolute;
    left: 0; right: 0; bottom: 0; height: 19px;
    background: var(--base-strip);
  }
</style>
</head>
<body>
  <main class="poster">
    <div class="offer-disc"></div>
    <div class="headline" aria-label="50% off">
      <span class="headline-figure">50</span>
      <span class="headline-percent">%</span>
      <span class="headline-off">OFF</span>
      <svg class="headline-slash" width="912" height="1200" aria-hidden="true">
        <line x1="364" y1="568" x2="691" y2="248" stroke="#ffffff" stroke-width="8"/>
      </svg>
    </div>
    <p class="offer-terms">50% OFF the marked price<br>of any <span class="tag-colour">blue</span> price tag.</p>
    <footer class="brand-panel">
      <span class="brand-dot" aria-hidden="true"></span>
      <span class="brand-name">Marla's Found Again</span>
    </footer>
    <div class="base-strip"></div>
  </main>
</body>
</html>
```